Business card design for new software start-up

This design is for a double-sided, colour business card. The requirements are as follows:
PREVIEW IMAGES:
The preview images of the card should be shown on a white background (i.e. no wood veneers etc).
The preview images for the front and back of the card should be presented top to bottom without overlapping.
OVERALL DESIGN:
Clean, crisp and simple
LOGO COLOURS:
Green - CMYK 50C 100Y (PMS 376)
Grey - CMYK 80K
CARD SIZES:
Trim Size (Card Size) 90mm x 55mm
Margin Size: 80mm x 45mm
Bleed Size: 96mm x 61mm (i.e. 3mm bleed)
The corners of the card should be SQUARE and NOT ROUNDED.
CARD ORIENTATION:
Landscape (i.e. horizontal).
FRONT OF CARD:
- White background
- uTrellow logo with tag line
- NodaKite logo scaled to a width of 1.25 inches and not as prominent as the uTrellow logo
- The NodaKite logo should be placed on a plain background, not overlapping any background images
- Details:
Orlando Pitkey
Founder and Chief Software Architect
uTrellow Pty Ltd
Suite 2704, 51-55 Harlow St
Sydney NSW 2000
Australia
M: +61 (0) 555 0142
E: orlando.pitkey@utrellow.example
www.utrellow.example
BACK OF CARD
- uTrellow logo without tag line
- www.utrellow.example
The back of the card should reflect the concept of being ahead of the curve in a simple or abstract way. Some possible ideas are as follows but other creative suggestions will also be considered:
1) A bell curve taking up the entire area, with the uTrellow logo on the right, near a position ahead of the curve;
2) A graphical, curved arrow with the uTrellow logo near the top of the arrow;
3) An abstract curve with the uTrellow logo near the top of the curve.
At least a portion of the background colour should consist of the logo's green colour using colour code CMYK 50C 100Y (PMS 376). For designs that place the logo over a green background, the colour of the dot over the first "i" may be changed so that it is still visible.
SOURCE FILES
Must be in AI format with 2 versions:
(1) With editable texts/fonts to allow for name and address changes in future;
(2) With all text converted to vectors/paths
PRINT FILES
Must be delivered in PDF, TIFF, JPG, EPS and PSD formats
Images should be 300 DPI
Updates
Revision to design for back of card:
The back of the card should also include the web address: www.utrellow.example
At least a portion of the background colour should consist of the logo's green colour. For designs that place the logo over a green background, the colour of the dot over the first "i" may be changed so that it is still visible.
Additional information:
1) The NodaKite logo should be placed on a plain background, not overlapping any background images;
2) The orientation of the card should be landscape (i.e. horizontal).

```html
<!DOCTYPE html>
<html lang="en">
<head>
<meta charset="utf-8">
<title>uTrellow business card</title>
<link href="https://fonts.googleapis.com/css2?family=Arimo:wght@700&family=Open+Sans:wght@300;400;700&display=swap" rel="stylesheet">
<style>
  :root {
    --page: #ffffff;
    --green-dark: #3f5a08;
    --green-mid: #7f9a06;
    --green-bright: #c5d80f;
    --glow: #f4f3a0;
    --white: #ffffff;
    --badge-dark: #1b3f86;
    --badge-light: #2a6bb4;
    --shadow: rgba(0,0,0,0.45);
  }
  html, body {
    margin: 0;
    padding: 0;
    width: 1200px;
    height: 900px;
    overflow: hidden;
    background: var(--page);
  }
  .canvas {
    position: relative;
    width: 1200px;
    height: 900px;
  }
  .card {
    position: absolute;
    width: 650px;
    height: 397px;
    overflow: hidden;
    box-shadow: 14px 14px 16px var(--shadow);
  }
  .card--front { left: 310px; top: 45px; }
  .card--back { left: 313px; top: 503px; height: 396px; background: var(--white); outline: 1px solid #222; }
  .card__art {
    position: absolute;
    inset: 0;
    width: 650px;
    height: 397px;
  }
  .wordmark {
    position: absolute;
    margin: 0;
    font-family: "Arimo", Arial, sans-serif;
    font-weight: 700;
    color: var(--white);
    letter-spacing: -2px;
    line-height: 1;
  }
  .card--front .wordmark { left: 38px; top: 38px; font-size: 70px; }
  .web {
    position: absolute;
    left: 41px;
    top: 100px;
    margin: 0;
    font-family: "Open Sans", Arial, sans-serif;
    font-size: 17px;
    letter-spacing: 3px;
    color: var(--white);
  }
  .card--back .wordmark { right: 148px; top: 38px; font-size: 60px; }
  .divider {
    position: absolute;
    left: 513px;
    top: 42px;
    width: 2px;
    height: 90px;
    background: var(--white);
  }
  .tagline {
    position: absolute;
    left: 530px;
    top: 44px;
    margin: 0;
    font-family: "Arimo", Arial, sans-serif;
    font-weight: 700;
    font-size: 13.5px;
    line-height: 17px;
    color: var(--white);
    text-transform: uppercase;
  }
  .details {
    position: absolute;
    right: 137px;
    top: 135px;
    margin: 0;
    text-align: right;
    font-family: "Open Sans", Arial, sans-serif;
    color: var(--white);
    font-weight: 300;
  }
  .details__name { font-weight: 700; font-size: 14.5px; line-height: 20px; margin: 0; }
  .details__role { font-size: 15px; line-height: 20px; margin: 0 0 14px; }
  .details__block { font-size: 12.5px; line-height: 17px; margin: 0 0 17px; font-style: normal; }
  .partner-badge {
    position: absolute;
    left: 37px;
    top: 284px;
    width: 173px;
    height: 75px;
    border-radius: 7px;
    background: linear-gradient(90deg, var(--badge-dark), var(--badge-light));
  }
</style>
</head>
<body>
<div class="canvas">

  <section class="card card--front" aria-label="Card back side">
    <svg class="card__art" viewBox="0 0 650 397" aria-hidden="true">
      <defs>
        <radialGradient id="frontGlow" cx="560" cy="250" r="600" gradientUnits="userSpaceOnUse">
          <stop offset="0" stop-color="var(--glow)"/>
          <stop offset="0.18" stop-color="var(--green-bright)"/>
          <stop offset="0.6" stop-color="var(--green-mid)"/>
          <stop offset="1" stop-color="var(--green-dark)"/>
        </radialGradient>
      </defs>
      <rect width="650" height="397" fill="url(#frontGlow)"/>
      <path d="M565 -5 C555 60 495 95 425 130 C330 178 318 305 390 352 C420 372 440 388 455 402"
            fill="none" stroke="var(--white)" stroke-width="22"/>
    </svg>
    <svg class="card__art" viewBox="0 0 650 397" role="img" aria-label="Photograph of a glowing light bulb">
      <defs>
        <radialGradient id="bulbGlow" cx="540" cy="250" r="110" gradientUnits="userSpaceOnUse">
          <stop offset="0" stop-color="#fffbd8" stop-opacity="0.95"/>
          <stop offset="0.5" stop-color="#f5ee8a" stop-opacity="0.55"/>
          <stop offset="1" stop-color="#e8e56a" stop-opacity="0"/>
        </radialGradient>
      </defs>
      <circle cx="540" cy="250" r="110" fill="url(#bulbGlow)"/>
    </svg>
    <p class="wordmark">uTrellow</p>
    <p class="web">www.utrellow.example</p>
  </section>

  <section class="card card--back" aria-label="Card front side">
    <svg class="card__art" viewBox="0 0 650 397" aria-hidden="true">
      <defs>
        <radialGradient id="backGlow" cx="230" cy="290" r="520" gradientUnits="userSpaceOnUse">
          <stop offset="0" stop-color="var(--glow)"/>
          <stop offset="0.2" stop-color="var(--green-bright)"/>
          <stop offset="0.6" stop-color="var(--green-mid)"/>
          <stop offset="1" stop-color="var(--green-dark)"/>
        </radialGradient>
      </defs>
      <path d="M120 0 L650 0 L650 397 L250 397 C252 305 215 262 160 236 C78 198 48 118 78 52 C88 28 104 10 120 0 Z"
            fill="url(#backGlow)"/>
    </svg>
    <p class="wordmark">uTrellow</p>
    <span class="divider"></span>
    <p class="tagline">Building<br>tomorrow's<br>software</p>
    <div class="details">
      <p class="details__name">Orlando Pitkey</p>
      <p class="details__role">Founder and Chief Software Architect</p>
      <address class="details__block">uTrellow Pty Ltd<br>Suite 2704, 51-55 Harlow St<br>Sydney NSW 2000<br>Australia</address>
      <p class="details__block">M: +61 (0) 555 0142<br>E: orlando.pitkey@utrellow.example</p>
    </div>
    <div class="partner-badge" role="img" aria-label="Partner programme badge"></div>
  </section>

</div>
</body>
</html>
```